Letterhead for Law Firm - Logo already prepared

I previously used to prepare a logo which I was quite pleased with, a copy is attached for your reference. I would like the font of the logo to be all the same size, rather than the 'S' and 'L' being larger than the other letters.
I have copies of the attached in other formats if necessary.
I need a letterhead prepared which is virtually identical to the draft attached, however I will be adding an address, phone number, fax number, mobile number and email. I will provide these details with whoever can assist me.
I will also be providing insurance details to be listed at the foot of the page.
Finally, I need the file to be supplied as a high resolution pdf with 2mm bleed.
If you require any further information, please do not hesitate to contact me.

```html
<!DOCTYPE html>
<html lang="en">
<head>
<meta charset="utf-8">
<title>Varnholt Legal – Letterhead</title>
<link href="https://fonts.googleapis.com/css2?family=Marcellus&family=Tinos&family=PT+Sans&display=swap" rel="stylesheet">
<style>
  :root {
    --orange-light: #f8961e;
    --orange-deep: #f05a28;
    --icon-orange: #e8662a;
    --ink: #1d1d1d;
    --text: #333333;
    --rule: #222222;
    --divider: #b5b5b5;
    --paper: #ffffff;
    --square: #4a64a8;
  }
  * { margin: 0; padding: 0; box-sizing: border-box; }
  html, body { width: 960px; height: 1200px; overflow: hidden; background: var(--paper); }
  .letterhead { position: relative; width: 960px; height: 1200px; background: var(--paper); }
  .side-band {
    position: absolute; left: 0; top: 0; width: 114px; height: 1200px;
    background: linear-gradient(180deg, var(--orange-light) 0%, #f37a22 35%, var(--orange-deep) 62%, var(--orange-deep) 100%);
  }
  .side-rule {
    position: absolute; left: 120px; top: 188px; width: 3px; height: 1012px; background: var(--rule);
  }
  .brand-disc {
    position: absolute; left: 31px; top: 19px; width: 176px; height: 176px;
    border-radius: 50%; background: var(--paper);
  }
  .firm-name {
    position: absolute; left: 200px; top: 88px;
    font-family: "Marcellus", serif; font-size: 50px; line-height: 1;
    color: var(--ink); letter-spacing: 1px; white-space: nowrap;
  }
  .contact {
    position: absolute; left: 757px; top: 49px; height: 126px;
    border-left: 1px solid var(--divider); padding-left: 8px; padding-top: 7px;
    list-style: none;
  }
  .contact li {
    display: flex; align-items: center; gap: 6px;
    font-family: "Tinos", serif; font-size: 14px; line-height: 16.4px; color: var(--text);
    white-space: nowrap;
  }
  .contact svg { width: 10px; height: 10px; flex: none; }
  .footer { position: absolute; left: 140px; top: 1144px; width: 800px; }
  .footer-address {
    font-family: "Tinos", serif; font-size: 14px; color: var(--text); line-height: 18px;
  }
  .footer-notes p {
    font-family: "PT Sans", sans-serif; font-size: 7.6px; line-height: 12px;
    color: var(--text); white-space: nowrap;
  }
</style>
</head>
<body>
<div class="letterhead">
  <div class="side-band"></div>
  <div class="side-rule"></div>
  <div class="brand-disc"></div>
  <h1 class="firm-name">VARNHOLT LEGAL</h1>

  <ul class="contact">
    <li>
      <svg viewBox="0 0 10 10" aria-hidden="true"><path d="M2.2 1 L4 2.6 L3.2 3.8 Q4.2 5.8 6.2 6.8 L7.4 6 L9 7.8 L7.8 9 Q3.8 8.6 1 2.2 Z" fill="var(--icon-orange)"/></svg>
      98-5120-3370
    </li>
    <li>
      <svg viewBox="0 0 10 10" aria-hidden="true"><rect x="2.5" y="0.5" width="5" height="9" rx="1" fill="var(--icon-orange)"/><rect x="3.4" y="1.6" width="3.2" height="4" fill="#fff"/></svg>
      12-4081-2265
    </li>
    <li>
      <svg viewBox="0 0 10 10" aria-hidden="true"><rect x="3" y="1" width="4" height="3" fill="var(--icon-orange)"/><rect x="0.5" y="4" width="9" height="4" rx="1" fill="var(--icon-orange)"/><rect x="2.5" y="7" width="5" height="2.5" fill="var(--icon-orange)"/></svg>
      12-4081-2265
    </li>
    <li>
      <svg viewBox="0 0 10 10" aria-hidden="true"><rect x="0.5" y="2" width="9" height="6.5" rx="1" fill="var(--icon-orange)"/><path d="M1 2.5 L5 5.6 L9 2.5" stroke="#fff" stroke-width="1" fill="none"/></svg>
      info@varnholtlegal.com
    </li>
    <li>
      <svg viewBox="0 0 10 10" aria-hidden="true"><circle cx="5" cy="5" r="4.2" fill="none" stroke="var(--icon-orange)" stroke-width="1"/><ellipse cx="5" cy="5" rx="1.8" ry="4.2" fill="none" stroke="var(--icon-orange)" stroke-width="0.8"/><line x1="0.8" y1="5" x2="9.2" y2="5" stroke="var(--icon-orange)" stroke-width="0.8"/></svg>
      www.varnholtlegal.com
    </li>
    <li>
      <svg viewBox="0 0 10 10" aria-hidden="true"><rect x="0.5" y="0.5" width="9" height="9" rx="1" fill="var(--square)"/></svg>
      /varnholtlegal
    </li>
  </ul>

  <footer class="footer">
    <p class="footer-address">Street Name, City Name, State, City Zip Code</p>
    <div class="footer-notes">
      <p>Professional indemnity insurance is held with an approved insurer under policy number PI-000000. Liability limited by a scheme approved under professional standards legislation for all practising solicitors.</p>
      <p>Our practice is a member of the regional law society. Client trust account details, registration numbers and complaint procedures are available on request from our office during normal business hours.</p>
    </div>
  </footer>
</div>
</body>
</html>
```